Car Show Event Signup (1 simple page)

We need a graphical design for a single page that is used for an automotive event ticket registration. It's for a car show event and needs a simple header and background design. We use Pavobooth.com for ticket booking service, and within this service we are able to upload a custom header, background, and manipulate CSS and other SIMPLE variables. Specific variables listed below in the "Must Have" field.

Here is a showcase of how other companies have their page. Useful for ideas:
http://www.pavobooth.com/showcase

Target Market(s)

An automotive car show company that targets young male adults.

Industry/Entity Type

Automotive

Requirements
Must have
• A) View the attached image "brushvault_parameters" for required parameters

B) Logo - View attached file "kreto show logo"

C) URL: www.KRETOshow.com

D) Header and/or background should have a mix of female models, TASTEFULLY modified Import & Domestic cars, bikes, and trucks.
Nice to have
• Would be nice to see an artistically blended in image into the header and/or background of an indoor people crowd around vehicles. Similar to the image visible on www.kretoshow.com

```html
<!DOCTYPE html>
<html lang="en">
<head>
<meta charset="utf-8">
<title>KRETO Show 2013 – Tickets</title>
<link href="https://fonts.googleapis.com/css2?family=Arimo:wght@400;700&display=swap" rel="stylesheet">
<style>
:root{
  --ink:#222;
  --muted:#333;
  --red:#c80000;
  --panel:#ededed;
  --rule:#e4e4e4;
  --card:#fff;
  --night:#000;
  --city-a:#1d3346;
  --city-b:#0b1824;
  --field:#ccc;
}
*{box-sizing:border-box;margin:0;padding:0}
html,body{width:1200px;height:2161px;overflow:hidden}
body{position:relative;background:var(--night);font-family:"Arimo",Arial,sans-serif;color:var(--ink)}
.a{position:absolute}
.city-scene{left:0;top:0;width:1200px;height:900px;
  background:linear-gradient(180deg,#2a4156 0%,var(--city-a) 25%,var(--city-b) 55%,var(--night) 100%)}
.car-photo{left:700px;top:0;width:460px;height:190px;border-radius:0 0 40px 120px;
  background:radial-gradient(ellipse at 60% 55%,#2a2f36 0%,#161a1f 55%,rgba(15,20,26,0) 80%)}
.brand{left:122px;top:92px;display:flex;align-items:center;gap:10px;
  font-weight:700;font-size:38px;color:#fff;letter-spacing:1px}
.brand-dot{width:30px;height:30px;border-radius:50%;background:var(--red)}
.card{left:120px;top:187px;width:959px;height:1942px;background:var(--card);border-radius:20px;overflow:hidden}
.intro{left:145px;top:226px;width:911px;font-size:16.5px;line-height:28.6px;color:var(--muted);text-align:justify}
.info{left:134px;top:389px;width:929px;height:226px;background:var(--panel);border-radius:22px}
.info-row{left:148px;font-size:15px;line-height:20px;display:flex}
.info-row .k{width:85px}
.info-row .c{width:19px}
.like{left:150px;top:570px;font-size:14px;display:flex;align-items:center;gap:6px;color:var(--muted)}
.like-btn{border:1px solid #c6cbd6;background:#f4f5f8;padding:1px 8px;border-radius:3px;color:#3b5998}
.like-count{border:1px solid #ccc;background:#fff;padding:1px 5px;font-size:12px}
.divider{left:658px;top:400px;width:3px;height:200px;background:linear-gradient(90deg,#ccc,#fff)}
.highlight{left:693px;top:433px;width:343px;font-size:18px;line-height:34px;color:var(--muted);text-align:justify}
.h{left:150px;font-size:17px;color:var(--muted)}
.h.small{font-size:15px}
.rule{left:150px;width:906px;height:1px;background:var(--rule)}
.t{font-size:15px;line-height:20px;color:var(--muted)}
.radio{display:inline-block;width:13px;height:13px;border-radius:50%;border:1px solid #999;background:#fff;vertical-align:-2px;margin-right:10px;position:relative}
.radio.on::after{content:"";position:absolute;left:3px;top:3px;width:5px;height:5px;border-radius:50%;background:#2a5f9e}
.check{display:inline-block;width:14px;height:14px;border:1px solid #999;background:#fff;vertical-align:-2px;margin-right:12px}
.price-tag{left:530px;top:745px;width:340px;height:40px;background:var(--red);border-radius:4px;color:#fff;font-size:14px;display:flex;align-items:center;justify-content:center}
.qty{left:150px;top:821px;width:66px;height:35px;border:1px solid var(--field);border-radius:3px;font-size:15px;display:flex;align-items:center;padding-left:16px;gap:10px}
.field{border:1px solid var(--field);border-radius:8px;background:#fff}
.apply{left:493px;top:893px;width:101px;height:38px;background:var(--red);color:#fff;border-radius:0 8px 8px 0;font-size:16px;display:flex;align-items:center;justify-content:center}
.buy{left:150px;top:1929px;width:128px;height:35px;background:var(--red);color:#fff;font-size:16px;display:flex;align-items:center;justify-content:center}
.footer{left:120px;top:1995px;width:959px;height:134px;background:linear-gradient(180deg,#fff 0%,#efefef 45%,#e2e2e2 100%);border-radius:0 0 20px 20px}
.badge{border-radius:40px;background:#fff;border:3px solid #8b0d14}
.partner{left:455px;top:2026px;width:277px;text-align:center;font-size:34px;font-weight:700;color:#3a7a2a}
</style>
</head>
<body>
<div class="a city-scene" role="img" aria-label="Night city skyline photo fading to black"></div>
<div class="a car-photo" role="img" aria-label="Dark sports coupe photographed from the rear"></div>
<div class="a brand"><span class="brand-dot"></span>KRETOSHOW</div>

<div class="a card"></div>

<p class="a intro">KRETO is proud to announce our arrival at the Harbor Bay Convention Center this January 26 2013 kicking off our 2013 KRETOshow tour celebrating all forms of motorsports in a festival environment welcoming enthusiasts from every reach of motorsports into a showcase featuring record breakers and head turners from top motorsports genres. Prepare to see the top racers and show cars from the KRETO series as well as competition boats, hot trucks both lifted and low.</p>

<div class="a info"></div>
<div class="a info-row" style="top:415px"><span class="k">Location</span><span class="c">:</span><span>Harbor Bay Convention Center</span></div>
<div class="a info-row" style="top:452px"><span class="k">Dates</span><span class="c">:</span><span>Saturday, Jan 26 2013, 3:00 PM - 11:00 PM</span></div>
<div class="a info-row" style="top:490px"><span class="k">Address</span><span class="c">:</span><span>2450 Exposition Way, Harbor Bay, FL 33190</span></div>
<div class="a info-row" style="top:526px"><span class="k">Directions</span><span class="c">:</span><span>Mapline, Routely, Findr, WayQuest</span></div>
<div class="a like"><span class="like-btn">Like</span><span class="like-count">3k</span><span>&nbsp;46 people like this. Sign Up to see what your friends like.</span></div>
<div class="a divider"></div>
<p class="a highlight">The only indoor event with DOMESTIC &amp; IMPORT makes of RACE &amp; SHOW cars. As well as Trucks &amp; Bikes. We'll be having unique award categories!</p>

<div class="a h" style="top:647px">Ticket Options</div>
<div class="a rule" style="top:689px"></div>
<div class="a t" style="left:150px;top:719px">Ticket for</div>
<div class="a t" style="left:152px;top:755px"><span class="radio on"></span>Attendee Tickets</div>
<div class="a t" style="left:344px;top:755px"><span class="radio"></span>Participant Tickets</div>
<div class="a price-tag">| Tickets = $25 | Group Discount (4+) = $20 |</div>
<div class="a qty">0 <span style="font-size:10px;color:#666">| ▾</span></div>
<div class="a t" style="left:230px;top:827px">Ticket Price One [$25.00]</div>
<div class="a t" style="left:483px;top:827px"><span class="check"></span>Convenience Fee</div>
<div class="a t" style="left:150px;top:902px">Coupon Code</div>
<div class="a field" style="left:248px;top:893px;width:250px;height:38px;border-radius:8px 0 0 8px"></div>
<div class="a apply">Apply</div>
<div class="a t" style="left:738px;top:902px;font-size:17px">Subtotal &nbsp;: &nbsp;$0.00</div>
<p class="a t" style="left:150px;top:962px;width:906px;font-size:14.5px;line-height:25px">Tickets are digital and delivered via e-mail. Please bring the printed ticket and an ID to the front entrance. All tickets have a bar code and will be scanned</p>
<div class="a rule" style="top:1036px"></div>

<div class="a h small" style="top:1069px">Ticket Buyer Information</div>
<div class="a t" style="left:150px;top:1130px">First Name *</div>
<div class="a field" style="left:281px;top:1122px;width:301px;height:37px"></div>
<div class="a t" style="left:150px;top:1178px">Last Name *</div>
<div class="a field" style="left:281px;top:1170px;width:301px;height:37px"></div>
<div class="a t" style="left:150px;top:1227px">Email Address *</div>
<div class="a field" style="left:281px;top:1218px;width:301px;height:37px"></div>
<div class="a t" style="left:150px;top:1276px">Confirm Email *</div>
<div class="a field" style="left:281px;top:1265px;width:301px;height:37px"></div>
<div class="a rule" style="top:1345px"></div>

<div class="a h small" style="top:1380px">Billing Information</div>
<div class="a t" style="left:150px;top:1432px">Payment Method &nbsp;&nbsp;&nbsp;<span class="radio on"></span>KRETO PayRoute</div>
<p class="a t" style="left:150px;top:1489px;width:906px;font-size:14.5px;line-height:24px">You will be redirected to PayRoute after pressing the button below. Please make sure to finish the transaction by completing the PayRoute form. You can use any credit card without needing a PayRoute account.</p>
<div class="a rule" style="top:1563px"></div>

<div class="a h small" style="top:1596px">Terms &amp; Conditions</div>
<div class="a t" style="left:150px;top:1644px;font-size:14.5px">YOU MUST bring the printed confirmation page which is delivered via e-mail.</div>
<div class="a t" style="left:150px;top:1668px;font-size:14.5px">There are NO REFUNDS or EXCHANGES.</div>
<div class="a t" style="left:150px;top:1700px;font-size:14.5px">Outside food and drinks are not allowed into the venue.</div>
<div class="a t" style="left:150px;top:1732px;font-size:14.5px">Ticket is only valid for a single day.</div>
<p class="a t" style="left:150px;top:1775px;width:906px;font-size:14.5px;line-height:25px">The holder of this ticket assumes all responsibilities for any risk of bodily harm or loss of property sustained while attending this event, and waives all rights to lay claim, for damages resulting from any cause whatsoever either before, during, or after this event.</p>
<div class="a t" style="left:150px;top:1847px"><span class="check"></span>I Agree to the Terms Above</div>
<div class="a rule" style="top:1899px"></div>
<div class="a buy">Buy Tickets</div>

<div class="a footer"></div>
<div class="a badge" style="left:151px;top:2015px;width:137px;height:64px"></div>
<div class="a partner">Pavobooth</div>
<div class="a" style="left:918px;top:2018px;width:122px;height:60px;background:#fff;border:3px solid #a30d14;border-radius:4px"></div>
</body>
</html>
```